Stationery Design needed for logo design project

This project is linked to Pediatric Therapy Clinic for children with autism and other special needs needs new logo design.

Our company needs a Stationery Design. Please refer to our original project in the link above.

Reason: Too much to do right now while enjoying Christmas with all my family!

```html
<!DOCTYPE html>
<html lang="en">
<head>
<meta charset="utf-8">
<title>Brightwell Kids – Stationery</title>
<link rel="stylesheet" href="https://fonts.googleapis.com/css2?family=Arimo:wght@400;700&display=swap">
<style>
  :root{
    --blue:#0a8fd8;
    --green:#adf032;
    --ink:#333333;
    --paper:#ffffff;
    --board:#e6e6e6;
    --board-top:#f2f2f2;
    --faint-blue:#e4f1fa;
  }
  *{margin:0;padding:0;box-sizing:border-box}
  html,body{width:1200px;height:1154px;overflow:hidden}
  body{position:relative;font-family:"Arimo",Arial,sans-serif;color:var(--ink);
    background:linear-gradient(#ececec,#e2e2e2)}
  .hero{position:absolute;left:0;top:0;width:1200px;height:201px;
    background:radial-gradient(ellipse at 50% 40%,var(--board-top),#e0e0e0)}
  .divider{position:absolute;left:0;top:203px;width:1200px;height:3px;background:#fafafa}
  .brand{position:absolute;display:flex;align-items:center}
  .brand-dot{border-radius:50%;background:var(--blue);flex:none}
  .brand-name{font-weight:700;color:var(--blue);letter-spacing:.02em;white-space:nowrap}
  .brand--hero{left:236px;top:58px}
  .brand--hero .brand-dot{width:70px;height:70px;margin-right:26px}
  .brand--hero .brand-name{font-size:62px}
  .sheet{position:absolute;background:var(--paper);box-shadow:0 2px 6px rgba(0,0,0,.12);overflow:hidden}
  .card-front{left:42px;top:296px;width:425px;height:244px}
  .card-back{left:42px;top:571px;width:425px;height:242px}
  .card-green{left:42px;top:846px;width:425px;height:241px;background:var(--green)}
  .letterhead{left:505px;top:276px;width:632px;height:809px}
  .card-front .brand{left:28px;top:26px}
  .brand--sm .brand-dot{width:30px;height:30px;margin-right:12px}
  .brand--sm .brand-name{font-size:24px}
  .holder-name{position:absolute;left:237px;top:117px;font-size:16px}
  .holder-role{position:absolute;left:211px;top:139px;width:214px;height:23px;background:var(--blue);
    color:#fff;font-size:16px;padding:2px 0 0 26px}
  .contacts{position:absolute;font-size:10px;line-height:18px;list-style:none}
  .contacts li{display:flex;align-items:center;gap:7px}
  .contacts svg{width:10px;height:10px;flex:none}
  .contacts .blank{width:10px}
  .card-front .c-left{left:48px;top:170px}
  .card-front .c-right{left:236px;top:170px}
  .card-back .brand{left:52px;top:88px}
  .brand--md .brand-dot{width:36px;height:36px;margin-right:14px}
  .brand--md .brand-name{font-size:29px}
  .faint-mark{position:absolute;border-radius:50%;background:var(--faint-blue)}
  .card-back .faint-mark{left:148px;top:34px;width:50px;height:50px}
  .band{position:absolute;left:0;bottom:0;width:100%;background:var(--blue)}
  .card-back .band{height:24px}
  .card-green .brand{left:52px;top:90px}
  .card-green .brand-dot,.card-green .brand-name{background:none}
  .card-green .brand-dot{background:#fff}
  .card-green .brand-name{color:#fff}
  .letterhead .brand{left:30px;top:22px}
  .letterhead .rule{position:absolute;left:303px;top:67px;width:306px;height:1px;background:var(--green)}
  .letterhead .contacts{font-size:7.5px;line-height:15px}
  .letterhead .contacts svg{width:8px;height:8px}
  .letterhead .c-left{left:415px;top:35px}
  .letterhead .c-right{left:535px;top:35px}
  .letterhead .faint-mark{left:56px;top:447px;width:113px;height:113px}
  .letterhead .band{height:27px}
</style>
</head>
<body>
  <header class="hero">
    <div class="brand brand--hero"><span class="brand-dot"></span><span class="brand-name">BRIGHTWELL KIDS</span></div>
  </header>
  <div class="divider"></div>

  <section class="sheet card-front" aria-label="Business card front">
    <div class="brand brand--sm"><span class="brand-dot"></span><span class="brand-name">BRIGHTWELL KIDS</span></div>
    <p class="holder-name">your name</p>
    <p class="holder-role">position</p>
    <ul class="contacts c-left">
      <li><svg viewBox="0 0 10 10"><path d="M5 1a3 3 0 0 1 3 3c0 2-3 5-3 5S2 6 2 4a3 3 0 0 1 3-3z" fill="var(--green)"/></svg>your address, address 1</li>
      <li><span class="blank"></span>your address, address 2</li>
      <li><svg viewBox="0 0 10 10"><circle cx="5" cy="5" r="4" fill="var(--green)"/></svg>www.yourwebsite.com</li>
    </ul>
    <ul class="contacts c-right">
      <li><svg viewBox="0 0 10 10"><path d="M3 1c3 1 4 5 1 8" stroke="var(--green)" stroke-width="1.6" fill="none"/></svg>+(000) 1234 5678</li>
      <li><svg viewBox="0 0 10 10"><rect x="2" y="1" width="6" height="3" fill="none" stroke="var(--green)"/><rect x="1" y="4" width="8" height="5" fill="var(--green)"/></svg>+(000) 1234 5678</li>
      <li><svg viewBox="0 0 10 10"><rect x="1" y="2" width="8" height="6" fill="none" stroke="var(--green)"/><path d="M1 2l4 3 4-3" stroke="var(--green)" fill="none"/></svg>name@emailaddress.com</li>
    </ul>
  </section>

  <section class="sheet card-back" aria-label="Business card back">
    <span class="faint-mark"></span>
    <div class="brand brand--md"><span class="brand-dot"></span><span class="brand-name">BRIGHTWELL KIDS</span></div>
    <div class="band"></div>
  </section>

  <section class="sheet card-green" aria-label="Business card reverse">
    <div class="brand brand--md"><span class="brand-dot"></span><span class="brand-name">BRIGHTWELL KIDS</span></div>
  </section>

  <section class="sheet letterhead" aria-label="Letterhead">
    <div class="brand brand--sm"><span class="brand-dot"></span><span class="brand-name">BRIGHTWELL KIDS</span></div>
    <div class="rule"></div>
    <ul class="contacts c-left">
      <li><svg viewBox="0 0 10 10"><path d="M5 1a3 3 0 0 1 3 3c0 2-3 5-3 5S2 6 2 4a3 3 0 0 1 3-3z" fill="var(--green)"/></svg>your address, address 1</li>
      <li><span class="blank" style="width:8px"></span>your address, address 2</li>
    </ul>
    <ul class="contacts c-right">
      <li><svg viewBox="0 0 10 10"><path d="M3 1c3 1 4 5 1 8" stroke="var(--green)" stroke-width="1.6" fill="none"/></svg>+(000) 1234 5678</li>
      <li><svg viewBox="0 0 10 10"><rect x="2" y="1" width="6" height="3" fill="none" stroke="var(--green)"/><rect x="1" y="4" width="8" height="5" fill="var(--green)"/></svg>+(000) 1234 5678</li>
    </ul>
    <span class="faint-mark"></span>
    <div class="band"></div>
  </section>
</body>
</html>
```